Swimming Pool Service business card needed!!!! Please

Hi Everyone! Thanks for looking at my contest. I PROMISE to provide excellent feedback during this process.

I am starting a new swimming pool cleaning business in San Diego, California and would like your help in making a business card for me.

I like easy to read, classy and sophisticated.

I am having a website designed and I'm looking for it to have pictures of really clean & clear pools.

I really like the blue on white color format, but open to other colors.

I do not have a logo, but the name of my company is GLIMMERTIDE POOL SERVICE.

My tag line is: Pools so clean, you can see yourself "in" them. (does not need to have the quotes around "in"...maybe just italics for this word IN?) You decide for me.

I would like to have a logo designed that incorporates some sort of easy to read letters. I do not want cursive (handwriting) letters. I thought about having a "reflection" of letters (mirror image), but think that this will be hard to read from far away. Maybe you can surprise me and come up with an idea that works using the a mirror image....but I'm not sure. I was leaning toward plain old BLOCK letters as I think it would be easy to read on my truck.

I would like to have the NAQTR and WBK logos on the back of the card. I have attached those two as files. You can put other things on the back as well, but I need these two logos on there. Or maybe put them on the front of the card if you have a better idea for the back of the card! :-)

Maybe blue on the back of the card and white on the front of the card? I don't know, I'm just thinking out loud.

I had another card done awhile ago called HARBORLINE TEES. I have uploaded a copy of that card for your reference. I don't want this card to be the same as my new company is a swimming pool cleaning company, but I wanted you to see what I liked in the past.

THANK YOU!!!!
Updates

Reason: Partner out of town and want their feedback....so need more time to decide and designs still coming in.

Industry/Entity Type

Business

Contact Information for Business Card

GLIMMERTIDE POOL SERVICE
Dale Wexby
Owner
4817 Quarry Bend Ave. #512
San Diego, CA 92417
858-291-6083
www.glimmertidepoolservice.example

Font styles to use
Sans Serif

Colors
0255a3
3176b5
ffffff

Requirements
Nice to have
• Some things to (possibly) add to back of card (in no particular order)
• WBK logo
• NAQTR logo
• Free Estimates
• Residential and Commercial Services
• Equipment Repairs
• Saltwater Systems
• Licensed, Bonded, Insured
• Family Owned and Operated
• No Contracts
• =======================
• Check out the FolioMint business card that i attached.
• i think they did this using a chrome overlay.
• Can any of you guys design that? or is that done at my printer?
• ==================
Should not have
• Hi Designers-
• The first round of cards came back and let's stay away from the light blue (powder blue) color. I don't like the look of it on the business cards.
• Also, the pool company JPG's that I attached are other logos of pool companies that I liked. I don't want them to be on my card. The only logos that should be on my card are the one you are going to come up with for my company, the WBK logo and the NAQTR logo.
• Lastly, no vertical cards and no split cards (logo on left, contact info on right side).
• Thanks much!

```html
<!DOCTYPE html>
<html lang="en">
<head>
<meta charset="utf-8">
<title>Glimmertide Pool Service – Business Card</title>
<link rel="stylesheet" href="https://fonts.googleapis.com/css2?family=Questrial&display=swap">
<style>
  :root {
    --backdrop: #e8e5e0;
    --card-blue: #1f50a0;
    --card-edge: rgba(255, 255, 255, 0.55);
    --ink-white: #ffffff;
    --ink-soft: rgba(255, 255, 255, 0.28);
    --badge-paper: #ffffff;
    --badge-blue: #0255a3;
    --badge-mid: #3176b5;
  }
  * { box-sizing: border-box; margin: 0; padding: 0; }
  html, body {
    width: 1200px;
    height: 873px;
    overflow: hidden;
    background: var(--backdrop);
    font-family: "Questrial", "Century Gothic", sans-serif;
    color: var(--ink-white);
  }
  .canvas { position: relative; width: 1200px; height: 873px; }

  .card {
    position: absolute;
    top: 325px;
    width: 435px;
    height: 249px;
    background: var(--card-blue);
    border: 1px solid var(--card-edge);
    box-shadow: 0 6px 14px rgba(0, 0, 0, 0.25);
    overflow: hidden;
  }
  .card--front { left: 155px; }
  .card--back { left: 631px; }

  .wordmark { position: absolute; left: 6px; top: 6px; width: 236px; }
  .wordmark__name {
    display: block;
    font-size: 33px;
    line-height: 1;
    letter-spacing: 0.5px;
  }
  .wordmark__tag {
    display: block;
    text-align: right;
    font-size: 14px;
    line-height: 1;
    margin-top: 2px;
    letter-spacing: 0.5px;
  }

  .contact-name {
    position: absolute;
    right: 22px;
    top: 8px;
    width: 190px;
    text-align: center;
    font-size: 28px;
    line-height: 1.1;
    padding-bottom: 4px;
    border-bottom: 1.5px solid var(--ink-white);
  }
  .contact-role {
    position: absolute;
    right: 28px;
    top: 50px;
    font-size: 18px;
  }
  .contact-phone {
    position: absolute;
    right: 14px;
    top: 80px;
    font-size: 19px;
  }
  .contact-web {
    position: absolute;
    left: 0;
    right: 0;
    top: 126px;
    text-align: center;
    font-size: 21px;
    line-height: 1;
  }
  .contact-web__reflection {
    display: block;
    color: var(--ink-soft);
    transform: scaleY(-0.7);
    transform-origin: top;
    margin-top: 24px;
  }
  .contact-address {
    position: absolute;
    left: 11px;
    bottom: 12px;
    font-size: 14.5px;
  }

  .services { position: absolute; left: 11px; top: 80px; }
  .services__lead { font-size: 19px; line-height: 1.2; margin-bottom: 2px; }
  .services__list { list-style: none; font-size: 15.5px; line-height: 22px; }
  .services__list li { padding-left: 12px; text-indent: -12px; }
  .services__list li::before { content: "- "; }

  .credentials { position: absolute; right: 6px; top: 120px; width: 198px; }
  .credentials__line { text-align: center; font-size: 15px; margin-bottom: 7px; }
  .credentials__badges {
    display: block;
    width: 198px;
    height: 100px;
    background: var(--badge-paper);
  }
</style>
</head>
<body>
<main class="canvas">

  <section class="card card--front" aria-label="Card front">
    <div class="wordmark">
      <span class="wordmark__name">GLIMMERTIDE</span>
      <span class="wordmark__tag">POOL SERVICE</span>
    </div>
    <p class="contact-name">Dale Wexby</p>
    <p class="contact-role">Owner</p>
    <p class="contact-phone">858-291-6083</p>
    <p class="contact-web">
      www.glimmertidepoolservice.example
      <span class="contact-web__reflection" aria-hidden="true">www.glimmertidepoolservice.example</span>
    </p>
    <p class="contact-address">4817 Quarry Bend Ave. #512 San Diego, CA 92417</p>
  </section>

  <section class="card card--back" aria-label="Card back">
    <div class="wordmark">
      <span class="wordmark__name">GLIMMERTIDE</span>
      <span class="wordmark__tag">POOL SERVICE</span>
    </div>
    <div class="services">
      <p class="services__lead">Free Estimates</p>
      <ul class="services__list">
        <li>Residential &amp;<br>Commercial Services</li>
        <li>Equipment Repairs</li>
        <li>Saltwater Systems</li>
        <li>Family Owned &amp; Operated</li>
        <li>No Contracts</li>
      </ul>
    </div>
    <div class="credentials">
      <p class="credentials__line">Licensed, Bonded, Insured</p>
      <svg class="credentials__badges" viewBox="0 0 198 100" role="img" aria-label="Certification badges: WBK and NAQTR">
        <rect width="198" height="100" fill="var(--badge-paper)"/>
        <circle cx="52" cy="50" r="40" fill="var(--badge-blue)"/>
        <circle cx="146" cy="50" r="40" fill="var(--badge-mid)"/>
      </svg>
    </div>
  </section>

</main>
</body>
</html>
```